Luxury Face Oil Label

I'm looking for a simple and sophisticated design for a natural face oil that will target the luxe market. It is a pure Natural product. I have attached the logo, Velumi Organics.

Here's the Copy

LUXE FACIAL OIL

Regenerate. Hydrate. Glow

100% Natural

30ml (1.01 oz)

A complex blend of Pure Oils including Marula, Sea Buckthorn, Rosehip, Neroli, Evening primrose, Argan, Calendula, Lavender, Jojoba, Grapeseed, Baobab, Moringa and Vitamin E oil.

Produced by
Brasso Kettle Ltd
P.O box 7925-00300
Nairobi, Kenya
www.velumiorganics.example

Target Market(s)

High end

Requirements
Must have
• Simple, Please consider the bottle, which is a 30ml clear glass bottle with a gold and white pump. Image attached.
Nice to have
• Very clean designs, not too much going on.
Should not have
• Leaves and nuts.

```html
<!DOCTYPE html>
<html lang="en">
<head>
<meta charset="utf-8">
<title>Velumi Organics – Luxe Facial Oil Label</title>
<link rel="stylesheet" href="https://fonts.googleapis.com/css2?family=Lato:wght@300;400&display=swap">
<style>
  :root {
    --canvas: #f5f5f7;
    --paper: #ffffff;
    --paper-shade: #ececec;
    --sage: #b8b99a;
    --ink: #54564a;
    --frame: #c5c7ad;
    --on-sage: #ffffff;
    --gold-1: #e9c05c;
    --gold-2: #fff6a6;
    --gold-3: #d9a84a;
    --gold-4: #6b4a1e;
    --gold-5: #b3893d;
  }
  * { box-sizing: border-box; margin: 0; padding: 0; }
  html, body { width: 1200px; height: 1060px; overflow: hidden; }
  body {
    background: var(--canvas);
    font-family: "Lato", sans-serif;
    font-weight: 300;
    position: relative;
  }
  .gold-band {
    background: linear-gradient(90deg, var(--gold-1) 0%, var(--gold-2) 22%, var(--gold-3) 45%, var(--gold-4) 55%, var(--gold-5) 68%, var(--gold-5) 100%);
  }
  .panel { position: absolute; display: flex; flex-direction: column; }
  .panel__white {
    background: linear-gradient(90deg, var(--paper-shade) 0%, var(--paper) 45%, var(--paper) 70%, var(--paper-shade) 100%);
    display: flex; align-items: center; justify-content: center;
  }
  .panel__sage { background: var(--sage); color: var(--on-sage); position: relative; }

  .brand {
    border: 1px solid var(--frame);
    outline: 1px solid var(--frame);
    outline-offset: 4px;
    display: flex; align-items: center; justify-content: center;
  }
  .brand__name {
    color: var(--ink);
    font-weight: 400;
    letter-spacing: 0.28em;
    text-transform: uppercase;
    text-align: center;
    line-height: 1.6;
  }

  .product-name { position: absolute; left: 0; right: 0; text-align: center; letter-spacing: 0.02em; }
  .volume { position: absolute; line-height: 1.2; }
  .claim { position: absolute; }

  /* Bottle label */
  .label { left: 170px; top: 477px; width: 300px; height: 393px; }
  .label .gold-band { height: 8px; }
  .label .panel__white { height: 240px; }
  .label .panel__sage { flex: 1; }
  .label .brand { width: 166px; height: 166px; }
  .label .brand__name { font-size: 15px; }
  .label .product-name { top: 22px; font-size: 18px; }
  .label .volume { left: 17px; top: 78px; font-size: 16px; }
  .label .claim { right: 12px; top: 98px; font-size: 16px; }

  /* Box front */
  .box { left: 600px; top: 90px; width: 400px; height: 780px; }
  .box .gold-band { height: 7px; }
  .box .panel__white { height: 538px; align-items: flex-start; padding-top: 172px; }
  .box .panel__sage { flex: 1; }
  .box .brand { width: 226px; height: 226px; }
  .box .brand__name { font-size: 21px; }
  .box .product-name { top: 75px; font-size: 22px; }
  .box .volume { left: 28px; top: 175px; font-size: 15px; }
  .box .claim { right: 28px; top: 196px; font-size: 21px; }
</style>
</head>
<body>
  <section class="panel label" aria-label="Bottle label">
    <div class="gold-band"></div>
    <div class="panel__white">
      <div class="brand"><p class="brand__name">Velumi<br>Organics</p></div>
    </div>
    <div class="gold-band"></div>
    <div class="panel__sage">
      <p class="product-name">LUXE FACIAL OIL</p>
      <p class="volume">30ml<br>(1.01 oz)</p>
      <p class="claim">100% Natural</p>
    </div>
  </section>

  <section class="panel box" aria-label="Box front panel">
    <div class="panel__white">
      <div class="brand"><p class="brand__name">Velumi<br>Organics</p></div>
    </div>
    <div class="gold-band"></div>
    <div class="panel__sage">
      <p class="product-name">LUXE FACIAL OIL</p>
      <p class="volume">30ml<br>(1.01 oz)</p>
      <p class="claim">100% Natural</p>
    </div>
  </section>
</body>
</html>
```